Have photos and logo just need help with web banner

Dimensions: 950 width by 425 height, pixels
Resolution: 92 DPI
Layout: Landscape
Format: JPG

Target Market(s)

Luxury market for women 28-55

Industry/Entity Type

Landscape

Number of Pages Required

1 page

Font styles to use
Script

Requirements
Must have
• Elegant, sophisticated feel
• Tagline: bags with a silver lining
Nice to have
• Shoes bag / has athletic, strong feel
Should not have
• Not cluttered. Not confusing.

```html
<!DOCTYPE html>
<html lang="en">
<head>
<meta charset="utf-8">
<title>Velmora — Banner</title>
<link rel="stylesheet" href="https://fonts.googleapis.com/css2?family=Lato:wght@400;700;900&family=Arimo:wght@400&family=Great+Vibes&display=swap">
<style>
  :root {
    --topbar-bg: #f4fbf1;
    --ink: #1c1c1c;
    --nav-bg: #000000;
    --button-bg: #ffffff;
    --button-active: #f8eef0;
    --stage-bg: #f8f2f2;
    --footer-top: #2b2e32;
    --footer-bottom: #040404;
    --logo-ink: #cfcfcf;
    --silver: #c9ccd1;
  }
  * { margin: 0; padding: 0; box-sizing: border-box; }
  html, body { width: 1200px; height: 537px; overflow: hidden; }
  body { position: relative; background: var(--stage-bg); font-family: "Lato", sans-serif; color: var(--ink); }

  .topbar { position: absolute; left: 0; top: 0; width: 1200px; height: 43px; background: var(--topbar-bg); font-size: 10px; }
  .topbar span, .topbar a { position: absolute; top: 15px; color: var(--ink); white-space: nowrap; }
  .contact-label { left: 44px; font-weight: 900; letter-spacing: 1px; }
  .contact-phone { left: 134px; letter-spacing: .4px; }
  .contact-sep { left: 238px; }
  .contact-email { left: 251px; text-decoration: underline; }
  .account-login { left: 979px; font-weight: 900; letter-spacing: 1.4px; }
  .account-sep { left: 1038px; font-weight: 900; }
  .account-register { left: 1056px; font-weight: 900; letter-spacing: 1.4px; }

  .navbar { position: absolute; left: 0; top: 43px; width: 1200px; height: 97px; background: var(--nav-bg); }
  .brand { position: absolute; left: 78px; top: 36px; display: flex; align-items: center; gap: 7px; color: var(--logo-ink); font-weight: 400; font-size: 15px; letter-spacing: 3px; }
  .brand-dot { width: 8px; height: 8px; border-radius: 50%; background: var(--logo-ink); }
  .nav-item { position: absolute; top: 24px; width: 129px; height: 45px; background: var(--button-bg); font-family: "Arimo", sans-serif; font-size: 15px; color: #000; display: flex; align-items: center; justify-content: center; text-decoration: none; }
  .nav-item.is-active { background: var(--button-active); align-items: flex-start; padding-top: 13px; }
  .nav-home { left: 250px; }
  .nav-classes { left: 400px; }
  .nav-news { left: 551px; }
  .nav-gallery { left: 700px; }
  .nav-contact { left: 847px; }

  .gallery-photo { position: absolute; }
  .photo-ring { left: 96px; top: 140px; width: 513px; height: 306px; background: linear-gradient(135deg, #5b6b80 0%, #8c7d78 45%, #6a6a5a 100%); }
  .photo-platform { left: 609px; top: 140px; width: 246px; height: 168px; background: linear-gradient(180deg, #4a4440 0%, #9a8f84 55%, #3a3634 100%); }
  .photo-ropes { left: 609px; top: 308px; width: 246px; height: 138px; background: linear-gradient(180deg, #7a2a2a 0%, #3a2020 40%, #151515 100%); }
  .photo-bench { left: 855px; top: 140px; width: 231px; height: 306px; background: linear-gradient(160deg, #d8d2c6 0%, #a99684 50%, #6b5440 100%); }

  .footer-band { position: absolute; left: 0; top: 446px; width: 1200px; height: 91px; background: linear-gradient(180deg, var(--footer-top), var(--footer-bottom)); display: flex; align-items: center; justify-content: center; }
  .tagline { font-family: "Great Vibes", cursive; font-weight: 400; font-size: 42px; line-height: 1; color: var(--silver); white-space: nowrap; }
</style>
</head>
<body>
  <header class="topbar">
    <span class="contact-label">CONTACT US:</span>
    <span class="contact-phone">+ 1 (555) 014 27 63</span>
    <span class="contact-sep">|</span>
    <a class="contact-email" href="#">hello@velmora.com</a>
    <span class="account-login">LOG IN</span>
    <span class="account-sep">|</span>
    <span class="account-register">REGISTER</span>
  </header>

  <nav class="navbar">
    <div class="brand"><span class="brand-dot"></span>VELMORA</div>
    <a class="nav-item nav-home" href="#">HOME</a>
    <a class="nav-item nav-classes" href="#">CLASSES</a>
    <a class="nav-item nav-news" href="#">NEWS</a>
    <a class="nav-item nav-gallery is-active" href="#">GALLERY</a>
    <a class="nav-item nav-contact" href="#">CONTACT</a>
  </nav>

  <main>
    <div class="gallery-photo photo-ring" role="img" aria-label="Two boxers sparring in a ring in front of a poster-covered gym wall"></div>
    <div class="gallery-photo photo-platform" role="img" aria-label="Black quilted sports bag resting on a subway platform"></div>
    <div class="gallery-photo photo-ropes" role="img" aria-label="Black quilted sports bag beside red boxing ring ropes"></div>
    <div class="gallery-photo photo-bench" role="img" aria-label="Black quilted sports bag on a wooden bench against a tiled wall"></div>
  </main>

  <footer class="footer-band">
    <p class="tagline">bags with a silver lining</p>
  </footer>
</body>
</html>
```